Brochure Design- Targeted at Property Developers

We are the largest Conveyancing (property law) firm in the state of Victoria, Australia.

We need a very sophisticated brochure to enable us to take the next step and compete with law firms for property developer clients.

Much about us can be found on our website (inlcuding logos, photos, etc) www.brindlecove.com.au but our business name is Brindlecove- Marlow Reach not just Brindlecove. ALSO I HAVE ATTACHED MANY PHOTOS OF OUR STAFF AND SOME LOGOS TO HELP!!

Size: fold (A3 double sided so that there is 4 A4 pages)

Copy:

This can be played with by the designer to spread across the 4 pages. Ideally the front page will be very minimalistic and not mention our brand (or at least the brand should not dominate):

Page 1: Do property developers have a genuine alternative to high legal fees?

Page 2 and 3:

- 100% of our developer clients recommend us
- We already look after the Conveyancing needs of more developers in Victoria than any other Conveyancing firm
- Industry benchmark off- the- plan contracts (tailored to the requirements of each development). Our special conditions (including variations, rebates and resale restrictions) are carefully chosen to protect the interests of our vendors while being commercially sensitive to ensure sales are not lost unnecessarily
- Expert in guiding developers from first time dual occupancies to seasoned developers of large scale land and highrise projects
- Our large team and highly refined systems ensure fastest possible settlement times after subdivision registration
- We are available to train your project marketers on completing and executing contracts so that sales are not delayed or lost
- Establishment of interest bearing trust accounts
- Before you buy a development site have us thoroughly investigate the contract and vendors statement. We can then conduct the purchase settlement on your behalf.
- We have the friendliest and most efficient staff. Every dealing you have with our dedicated Development Division will be prompt, professional and impressive. You will never need to follow us up!
- Highly experienced Conveyancers with the security of full Solicitor support

Please consider us next time you need Conveyancing.

Services options:
- Use us from contract preparation to settlement or;
- Have your Solicitor prepare the contract and use us as an alternative for the settlement stage only. Many Solicitors recommend us for this service already
- Fast subdivision lodgements (including obtaining mortgagee’s consent, Solicitor preparation of Land Titles Office application, owners corporation establishment)

Page 4: Just our contact details (see our website)

The design should make us look highly professional, conservative, yet cutting edge.
Updates

Target Market(s)

Property developers of small to medium sized land and unit developments

Industry/Entity Type

Security

Requirements
Must have
• - Our logo and contact details as well as the copy above.
Nice to have
• - Pictures of land sites, highrise buildings under construction
Should not have
• I really dislike overly corny photos where everyone is fake and smiling. Other photos would be great but not too cheesy.

```html
<!DOCTYPE html>
<html lang="en">
<head>
<meta charset="utf-8">
<title>Brindlecove- Marlow Reach — Developer Brochure Cover</title>
<link href="https://fonts.googleapis.com/css2?family=Arimo:wght@400;700&display=swap" rel="stylesheet">
<style>
  :root{
    --royal:#1023b9;
    --sky:#c1def0;
    --mid:#6890d8;
    --signal:#f31a0c;
    --ink:#1a1a1a;
    --paper:#ffffff;
    --rule:#8a8a8a;
    --photo-warm:#b48a6c;
    --photo-soft:#d7c2b4;
  }
  *{box-sizing:border-box;margin:0;padding:0}
  html,body{width:1200px;height:814px;overflow:hidden;background:var(--paper)}
  body{font-family:"Arimo",Arial,Helvetica,sans-serif;color:var(--ink)}
  .spread{position:relative;width:1200px;height:814px;border:1px solid #cfcfcf;overflow:hidden}
  .block{position:absolute}
  .fold{position:absolute;left:600px;top:0;width:1px;height:814px;background:var(--rule);z-index:5}
  .corner-tab{left:1100px;top:0;width:100px;height:108px;background:var(--signal);border-bottom-left-radius:16px}
  .field-royal{left:152px;top:48px;width:858px;height:530px;background:var(--royal)}
  .strip-sky{left:1010px;top:48px;width:190px;height:245px;background:var(--sky)}
  .strip-royal{left:1010px;top:293px;width:190px;height:224px;background:var(--royal)}
  .panel-sky{left:320px;top:293px;width:690px;height:285px;background:var(--sky);border-top-left-radius:26px}
  .tab-mid{left:525px;top:578px;width:289px;height:54px;background:var(--mid)}
  .tab-mid::before,.tab-mid::after{content:"";position:absolute;top:0;width:14px;height:14px;background:var(--paper)}
  .tab-mid::before{left:0;border-top-right-radius:0;clip-path:none;background:radial-gradient(circle at 0 100%,transparent 14px,transparent 14px)}
  .tile-sky{left:1030px;top:645px;width:127px;height:139px;background:var(--sky);border-top-left-radius:18px}
  .headline{position:absolute;left:604px;top:128px;width:400px;text-align:center;color:var(--sky);font-size:19.5px;line-height:24px;font-weight:400}
  .portraits{position:absolute;left:602px;top:334px;width:524px;height:188px;background:var(--paper);display:flex;gap:4px;padding:4px}
  .portrait{flex:1;border-bottom-right-radius:14px}
  .portrait--one{background:linear-gradient(160deg,#8d6a4c,var(--photo-warm) 55%,#5a4a3e)}
  .portrait--two{background:linear-gradient(160deg,#e8e4e2,var(--photo-soft) 55%,#4f6f9a)}
  .portrait--three{background:linear-gradient(160deg,#3a2a24,#c79a86 55%,#3b3432)}
  .brandmark{position:absolute;left:152px;top:605px;width:95px;height:40px;background:var(--royal);color:var(--paper);font-size:10px;line-height:12px;padding:7px 0 0 6px}
  .contact{position:absolute;left:152px;top:655px;font-size:9.5px;line-height:11.6px;color:var(--ink)}
  .contact p+p{margin-top:11.6px}
</style>
</head>
<body>
  <main class="spread">
    <div class="block field-royal"></div>
    <div class="block strip-sky"></div>
    <div class="block strip-royal"></div>
    <div class="block panel-sky"></div>
    <div class="block tab-mid"></div>
    <div class="block corner-tab"></div>
    <div class="block tile-sky"></div>

    <h1 class="headline">Do property developers<br>have a genuine alternative<br>to high legal fees?</h1>

    <div class="portraits">
      <div class="portrait portrait--one" role="img" aria-label="Portrait photo of a smiling staff member with long auburn hair"></div>
      <div class="portrait portrait--two" role="img" aria-label="Portrait photo of a smiling staff member with curly brown hair"></div>
      <div class="portrait portrait--three" role="img" aria-label="Portrait photo of a smiling staff member with dark hair"></div>
    </div>

    <div class="brandmark">Brindlecove<br>Marlow Reach</div>

    <address class="contact" style="font-style:normal">
      <p>Level 7, 14 Alder Crescent, Marlow Reach 3104 Victoria<br>
      Australia (Off Wattle Road)PO Box 4182<br>
      Wattle Road Central Marlow Reach 8108<br>
      DX Postal: DX 41730, South Marlow Reach</p>
      <p>Phone: (03) 5550 1234,<br>
      International: +61 3 5550 1234<br>
      Fax: (03) 5550 1299,<br>
      International Fax: +61 3 5550 1299<br>
      Email: marlowreach@brindlecove.com.au</p>
    </address>

    <div class="fold"></div>
  </main>
</body>
</html>
```